GREEN WILLOW LICE REMOVAL labels

I need a label design for our MINT REPELLING SHAMPOO (LICE PREVENTION).
It also includes our MINT REPELLING CONDITIONER (LICE PREVENTION) and our MINT SPRAY (LICE PREVENTION) also includes LICE & NIT ELIMINATING MOUSSE (LICE TREATMENT) and a LICE ELIMINATOR 100% Dimethicone oil (LICE TREATMENT). The shampoo and conditioner are sulfate free, contains peppermint and other essential oils and is safe for the entire family. Label should be simple, modern and high end looking. Fun is good too if it looks nice!

Target Market(s)

Kids and Adults

Industry/Entity Type

Hair Care Product

Font styles to use
Sans Serif
Decorative

Requirements
Must have
• -Words that should be used: safe, non toxic, sulfate free, essential oils, pesticide free. - Naturally removes lice, super lice & nits are great words for the lice & nit eliminating mousse and treatment oil 100% Dimethicone oil
- On a side note there are no essential oils in the lice & nit eliminating mousse or treatment oil 100% Dimethicone oil
Nice to have
• Earth tone colors if possible
Kid safe, no fillers, colors or scents
100% effective (even against super lice)
8oz labels and 4oz labels
Should not have
• No pictures of lice

```html
<!DOCTYPE html>
<html lang="en">
<head>
<meta charset="utf-8">
<title>Green Willow Lice Removal – Mint Repelling Labels</title>
<link rel="stylesheet" href="https://fonts.googleapis.com/css2?family=Montserrat:wght@400;500;600&display=swap">
<style>
  :root {
    --canvas-bg: #f4f8f4;
    --mint-pale: #eef5f2;
    --mint-mid: #b9d9cf;
    --mint-teal: #5c9a92;
    --green-bright: #4fb25d;
    --green-mid: #3d9c52;
    --green-deep: #2e7f43;
    --ink-green: #2f7a4a;
    --ink-dark: #1f5a36;
    --badge-red: #d64a2a;
    --white: #ffffff;
  }
  * { box-sizing: border-box; margin: 0; padding: 0; }
  html, body { width: 1200px; height: 1000px; overflow: hidden; }
  body {
    background: var(--canvas-bg);
    font-family: "Montserrat", Arial, sans-serif;
    display: flex;
    align-items: center;
    justify-content: center;
    gap: 60px;
  }
  .label {
    position: relative;
    width: 440px;
    height: 680px;
    border-radius: 26px;
    overflow: hidden;
    box-shadow: 0 10px 30px rgba(40, 90, 60, 0.15);
  }
  .label--shampoo {
    background:
      radial-gradient(circle at 70% 45%, rgba(92,154,146,0.55), transparent 55%),
      radial-gradient(circle at 30% 80%, rgba(185,217,207,0.7), transparent 50%),
      linear-gradient(180deg, var(--mint-pale) 0%, #e2efe9 50%, #f3f8f5 100%);
  }
  .label--conditioner {
    background:
      radial-gradient(circle at 30% 70%, rgba(46,127,67,0.45), transparent 55%),
      linear-gradient(180deg, var(--green-bright) 0%, var(--green-mid) 55%, #45a857 100%);
  }
  .brand {
    position: absolute;
    top: 58px;
    left: 0;
    right: 0;
    display: flex;
    flex-direction: column;
    align-items: center;
    gap: 12px;
  }
  .brand__dot {
    width: 70px;
    height: 70px;
    border-radius: 50%;
    background: var(--white);
  }
  .brand__name {
    font-size: 13px;
    font-weight: 600;
    letter-spacing: 3px;
    color: var(--ink-dark);
  }
  .label--conditioner .brand__name { color: var(--white); }
  .leaf-art {
    position: absolute;
    top: 220px;
    right: -10px;
    width: 200px;
    height: 260px;
    border-radius: 50% 40% 50% 45%;
    background: radial-gradient(ellipse at 50% 50%, rgba(255,255,255,0.35), rgba(255,255,255,0.05) 70%);
  }
  .title {
    position: absolute;
    top: 330px;
    left: 40px;
    font-size: 27px;
    font-weight: 600;
    line-height: 1.25;
    letter-spacing: 1.5px;
    color: var(--ink-green);
  }
  .label--conditioner .title { color: var(--ink-dark); }
  .copy {
    position: absolute;
    top: 460px;
    left: 40px;
    right: 30px;
    font-size: 12.5px;
    font-weight: 400;
    line-height: 1.45;
    color: var(--ink-green);
  }
  .label--conditioner .copy { color: var(--ink-dark); }
  .claims {
    position: absolute;
    top: 540px;
    left: 40px;
    right: 20px;
    font-size: 10.5px;
    font-weight: 500;
    color: var(--ink-dark);
    white-space: nowrap;
  }
</style>
</head>
<body>
  <section class="label label--shampoo">
    <div class="brand">
      <span class="brand__dot"></span>
      <span class="brand__name">GREEN WILLOW LICE REMOVAL</span>
    </div>
    <div class="leaf-art" role="img" aria-label="Line drawing of mint leaves"></div>
    <h1 class="title">MINT REPELLING<br>SHAMPOO</h1>
    <p class="copy">Naturally removes lice<br>super lice &amp; nits are great words for the lice<br>&amp; nit eliminating mousse and treatment oil %100 Dimethicone</p>
    <p class="claims">safe | non toxic | sulfate free | essential oils | pesticide free</p>
  </section>

  <section class="label label--conditioner">
    <div class="brand">
      <span class="brand__dot"></span>
      <span class="brand__name">GREEN WILLOW LICE REMOVAL</span>
    </div>
    <div class="leaf-art" role="img" aria-label="Line drawing of mint leaves"></div>
    <h1 class="title">MINT REPELLING<br>CONDITIONER</h1>
    <p class="copy">Naturally removes lice<br>super lice &amp; nits are great words for the lice<br>&amp; nit eliminating mousse and treatment oil %100 Dimethicone</p>
    <p class="claims">safe | non toxic | sulfate free | essential oils | pesticide free</p>
  </section>
</body>
</html>
```